Brindle's Homes website

We need a simple website for our property investment business in the UK. We basically need our contact details and brief description.We have the company logo already done (via ArtPlinth) so please use these:https://drive.google.com/drive/folders/1szJ3iRhelElZ40NIFT7w-c14MaY3Y_oV?usp=sharingYou could use some stock photos of UK houses for now.Let me know when to provide more detailed descriptions, etc

Coding

Coded - Design and coding required

Number of Pages Required

1 page

Colors

Designer to choose colors to be used in the design.

```html
<!DOCTYPE html>
<html lang="en">
<head>
<meta charset="utf-8">
<title>Brindle's Homes</title>
<link rel="stylesheet" href="https://fonts.googleapis.com/css2?family=Cormorant+Garamond:ital,wght@1,500&family=Poppins:wght@400;500;600&family=Roboto+Condensed:wght@400&family=Roboto+Slab:wght@400&display=swap">
<style>
:root{
  --ink:#1b1b1b;
  --text:#4a4a4a;
  --muted:#8a8a8a;
  --line:#dcdcdc;
  --panel:#ececec;
  --dark:#1c1c1c;
  --darker:#111;
  --white:#fff;
  --accent:#2f5f8a;
}
*{margin:0;padding:0;box-sizing:border-box}
html,body{width:1200px;height:3328px;overflow:hidden;background:var(--white)}
body{position:relative;font-family:'Poppins',sans-serif;color:var(--text)}
.abs{position:absolute}
.script{font-family:'Cormorant Garamond',serif;font-style:italic;font-weight:500;color:var(--ink);text-align:center;position:absolute;left:0;width:1200px}
.brand{display:flex;align-items:center;gap:8px;font-family:'Poppins',sans-serif;font-weight:600;color:var(--ink);white-space:nowrap}
.brand .mark{width:14px;height:14px;background:currentColor}

/* header */
.site-header{position:absolute;left:0;top:0;width:1200px;height:83px;background:var(--white)}
.site-header .brand{position:absolute;left:142px;top:28px;font-size:20px}
.nav{position:absolute;top:38px;font-family:'Roboto Slab',serif;font-size:16px;color:var(--ink)}
.nav.active{border-bottom:1px solid var(--ink);padding-bottom:2px}
.nav-phone{position:absolute;left:900px;top:36px;display:flex;align-items:center;gap:8px;font-size:17px;color:var(--ink)}

/* hero */
.hero{position:absolute;left:0;top:83px;width:1200px;height:562px;background:linear-gradient(180deg,#6f9fd8 0%,#a9c7ea 35%,#b8745a 60%,#5d7a3e 85%,#4a5a3a 100%)}
.hero-title{position:absolute;right:143px;top:94px;text-align:right;font-family:'Poppins',sans-serif;font-weight:500;font-size:37px;line-height:49px;color:var(--darker)}
.hero-arrow{position:absolute;top:270px;width:32px;height:24px;background:#2a2a2a;display:flex;align-items:center;justify-content:center}

/* services */
.service{position:absolute;top:810px;width:320px;height:140px}
.service .panel{position:absolute;left:0;top:12px;width:150px;height:128px;background:var(--panel)}
.service .icon{position:absolute;left:52px;top:68px}
.service .label{position:absolute;left:141px;top:85px;padding-left:10px;font-size:19px;font-weight:500;line-height:24px;color:#333;white-space:nowrap}

/* about */
.about-photo{position:absolute;left:142px;top:1132px;width:447px;height:445px;border:3px solid #333;background:linear-gradient(160deg,#c9c3b6 0%,#e3e6ea 45%,#8d9ba8 70%,#6d8c4a 100%)}
.about-body{position:absolute;left:630px;top:1140px;width:420px}
.about-body h2{font-family:'Cormorant Garamond',serif;font-style:italic;font-weight:500;font-size:39px;color:var(--ink);margin-bottom:12px;line-height:44px}
.about-body p{font-size:12.8px;line-height:23px;color:var(--text);margin-bottom:8px}
.about-body p.lead{font-size:15.5px;font-weight:500;line-height:28px;color:var(--ink);margin-top:4px}

/* why choose */
.why{position:absolute;left:0;top:1664px;width:1200px;height:444px;background:linear-gradient(100deg,#3a3a3a 0%,#262626 40%,#353535 70%,#4a4a4a 100%);overflow:hidden}
.why-photo{position:absolute;left:0;top:0;width:1200px;height:444px;background:radial-gradient(ellipse at 30% 40%,rgba(90,100,120,.35),transparent 60%)}
.why .title{color:var(--white);top:88px;font-size:39px}
.feature{position:absolute;font-family:'Roboto Condensed',sans-serif;color:var(--white);width:250px}
.feature h3{font-weight:400;font-size:17px;line-height:20px}
.feature p{font-size:12px;line-height:17px;color:#ddd}
.feature.right{text-align:right}
.why .brand{position:absolute;left:0;width:1200px;justify-content:center}

/* intro */
.intro{position:absolute;left:159px;top:2257px;width:878px;text-align:center;font-size:13px;line-height:23px;color:var(--text)}

/* contact */
.desk{position:absolute;left:0;top:2465px;width:1200px;height:552px;background:linear-gradient(180deg,#eef0f2 0%,#f7f7f7 60%,#e8e9ea 100%)}
.site-footer{position:absolute;left:0;top:3017px;width:1200px;height:311px;background:var(--dark)}
.form-card{position:absolute;left:269px;top:2649px;width:663px;height:465px;background:var(--white);border-radius:3px;box-shadow:0 2px 12px rgba(0,0,0,.12)}
.form-card h2{position:absolute;left:0;width:663px;top:66px;text-align:center;font-family:'Cormorant Garamond',serif;font-style:italic;font-weight:500;font-size:37px;color:var(--ink)}
.form-card .rule{position:absolute;left:301px;top:125px;width:58px;height:2px;background:var(--accent)}
.form-card .note{position:absolute;left:60px;width:543px;top:143px;text-align:center;font-size:12.5px;line-height:24px}
.field{position:absolute;border:1px solid var(--line);font-size:11px;color:var(--muted);padding:10px 14px}
.submit{position:absolute;left:275px;top:360px;width:112px;height:34px;border-radius:17px;background:var(--darker);color:var(--white);font-size:15px;display:flex;align-items:center;justify-content:center;gap:6px}
.form-card .fold{position:absolute;left:0;bottom:0;width:0;height:0;border-left:34px solid #888;border-top:34px solid transparent}

.contact-item{position:absolute;top:3207px;display:flex;align-items:center;gap:10px;color:var(--white);font-size:14px;line-height:17px}
.site-footer .brand{position:absolute;left:866px;top:200px;color:var(--white);font-size:22px;font-weight:500}
.bottom-bar{position:absolute;left:0;top:3290px;width:1200px;height:38px;background:var(--darker)}
.copyright{position:absolute;left:143px;top:3298px;font-size:14px;color:#ddd}
.social{position:absolute;top:3296px;width:26px;height:26px;border-radius:50%;background:#5c6f8a}
</style>
</head>
<body>

<header class="site-header">
  <div class="brand"><span class="mark"></span>Brindle's Homes</div>
  <span class="nav active" style="left:616px">Home</span>
  <span class="nav" style="left:692px">About Us</span>
  <span class="nav" style="left:791px">Contact Us</span>
  <div class="nav-phone">
    <svg width="26" height="26" viewBox="0 0 26 26"><circle cx="13" cy="13" r="12" fill="none" stroke="#1b1b1b" stroke-width="1.5"/><path d="M9 7c-2 2-1 7 3 11 2 2 4 2 5 1l-2-3-2 1c-1-1-3-3-3-5l1-1-2-4z" fill="#1b1b1b"/></svg>
    123-456-7890
  </div>
</header>

<section class="hero" role="img" aria-label="Photo of a row of red-brick London houses under a blue sky">
  <h1 class="hero-title">We are Property<br>Management Company<br>in London, UK</h1>
  <div class="hero-arrow" style="left:4px"><svg width="10" height="12"><path d="M7 1L2 6l5 5" stroke="#fff" stroke-width="2" fill="none"/></svg></div>
  <div class="hero-arrow" style="left:1164px"><svg width="10" height="12"><path d="M3 1l5 5-5 5" stroke="#fff" stroke-width="2" fill="none"/></svg></div>
</section>

<h2 class="script" style="top:720px;font-size:37px">We Offers Assistance &amp; Expertise To</h2>

<div class="service" style="left:170px">
  <div class="panel"></div>
  <svg class="icon" width="52" height="66" viewBox="0 0 52 66"><path d="M4 30L26 12l22 18" stroke="#111" stroke-width="4" fill="none"/><rect x="12" y="30" width="28" height="22" fill="none" stroke="#111" stroke-width="4"/><rect x="22" y="38" width="8" height="14" fill="#111"/><path d="M2 58c10 6 38 6 48 0" stroke="#111" stroke-width="4" fill="none"/><path d="M8 6c10-6 28-6 36 0" stroke="#111" stroke-width="4" fill="none"/></svg>
  <div class="label">Ground<br>Rent Collection</div>
</div>
<div class="service" style="left:505px">
  <div class="panel"></div>
  <svg class="icon" width="66" height="60" viewBox="0 0 66 60" style="left:28px"><path d="M16 24L38 6l22 18v16H16z" fill="#111"/><rect x="34" y="28" width="8" height="12" fill="#fff"/><path d="M2 40h20c6 0 10 4 16 4h14c4 0 4 6 0 6H30l22 2 12-8 2 4-14 10H2z" fill="#111"/></svg>
  <div class="label">Property<br>Insurance</div>
</div>
<div class="service" style="left:810px">
  <div class="panel"></div>
  <svg class="icon" width="64" height="64" viewBox="0 0 64 64" style="left:38px;top:70px"><circle cx="42" cy="20" r="18" fill="none" stroke="#111" stroke-width="3"/><rect x="32" y="18" width="6" height="12" fill="#111"/><rect x="40" y="12" width="6" height="18" fill="#111"/><rect x="48" y="8" width="6" height="22" fill="#111"/><circle cx="14" cy="20" r="7" fill="#111"/><path d="M4 30h20v20h-6v14h-8V50H4z" fill="#111"/><circle cx="28" cy="48" r="8" fill="#111"/></svg>
  <div class="label">Property<br>Accounting</div>
</div>

<h2 class="script" style="top:972px;font-size:37px">Contact Us Today - 123.456.7890</h2>

<div class="about-photo" role="img" aria-label="Portrait photo of a smiling estate agent in shirt and tie holding a folder"></div>
<div class="about-body">
  <h2>About Brindle's Homes</h2>
  <p>Lorem ipsum dolor sit amet, consectetuer adipiscing elit, sed reederiam nonummy nibh euismod tincidunt ut laoreet dolore lor emsmagna aliquam erat volutpat. Ut wisi enim fdaad minim veniam, quis nostrud exerci tation ullamcorper suscipit lobortis nisl ut aliquip ex ea commodo consequat.</p>
  <p>Duis autem vel eum iriure dolor in hendrerit in vulputate velit re esse molestie consequat, vel illum dolore eu feugiat nulla facilisis at vero eros et accumsan et iusto odio dignissim qui blandit rer praesent luptatum zzril delenit augue duis dolore te feugait nulla ptatum zzril delenit augue duis dolo facilisi.</p>
  <p>Duis autem vel eum iriure dolor in hendrerit in vulputate velit re esse molestie consequat, vel illum dolore eu feugiat nulla facilisis at vero eros et .</p>
  <p class="lead">Get the support you need now. Contact our 24/7 support line to get started.</p>
</div>

<section class="why">
  <div class="why-photo" role="img" aria-label="Darkened photo of a businessman in a suit with building sketches"></div>
  <h2 class="script title">Why Choose Us</h2>
  <svg class="abs" style="left:0;top:0" width="1200" height="444" viewBox="0 0 1200 444">
    <path d="M446 444A155 160 0 0 1 754 444" fill="#fff" stroke="#999" stroke-width="8"/>
    <g stroke="#aaa" stroke-dasharray="2 3" stroke-width="1.5">
      <line x1="539" y1="225" x2="562" y2="292"/><line x1="660" y1="225" x2="640" y2="292"/>
      <line x1="441" y1="274" x2="491" y2="331"/><line x1="758" y1="274" x2="708" y2="331"/>
      <line x1="391" y1="367" x2="446" y2="390"/><line x1="807" y1="367" x2="744" y2="390"/>
    </g>
    <g fill="#fff" stroke="#777" stroke-width="2">
      <circle cx="562" cy="292" r="5"/><circle cx="640" cy="292" r="5"/><circle cx="491" cy="331" r="5"/><circle cx="708" cy="331" r="5"/><circle cx="446" cy="390" r="5"/><circle cx="744" cy="390" r="5"/>
    </g>
    <g fill="#fff" stroke="#bbb" stroke-width="3">
      <circle cx="539" cy="225" r="36"/><circle cx="660" cy="225" r="36"/><circle cx="441" cy="274" r="36"/><circle cx="758" cy="274" r="36"/><circle cx="391" cy="367" r="36"/><circle cx="807" cy="367" r="36"/>
    </g>
    <g fill="#222">
      <path d="M527 212c-4 4-2 14 6 22s16 10 20 6l-5-7-5 2c-3-2-8-7-9-10l2-4z"/><circle cx="550" cy="214" r="9"/>
      <circle cx="660" cy="216" r="8"/><path d="M646 244c0-10 6-16 14-16s14 6 14 16z"/><circle cx="672" cy="208" r="7" fill="none" stroke="#222" stroke-width="2"/>
      <circle cx="434" cy="280" r="9"/><circle cx="450" cy="266" r="6"/>
      <circle cx="391" cy="363" r="10"/><rect x="386" y="374" width="10" height="6"/>
      <rect x="744" y="262" width="24" height="22" fill="none" stroke="#222" stroke-width="2.5"/><circle cx="770" cy="284" r="8" fill="none" stroke="#222" stroke-width="2.5"/>
      <circle cx="800" cy="358" r="6"/><circle cx="814" cy="366" r="6"/><path d="M790 382c0-10 20-10 20 0z"/><path d="M804 388c0-10 20-10 20 0z"/>
    </g>
  </svg>
  <div class="feature right" style="left:236px;top:158px"><h3>Unbiased Recommendations</h3><p>Lorem ipsum dolor sit mork<br>adipiscing sed diam</p></div>
  <div class="feature" style="left:700px;top:158px"><h3>Expert Guidance</h3><p>Lorem ipsum dolor sit mork<br>adipiscing sed diam</p></div>
  <div class="feature right" style="left:138px;top:252px"><h3>Unparalleled Service</h3><p>Lorem ipsum dolor sit mork<br>adipiscing sed diam</p></div>
  <div class="feature" style="left:806px;top:259px"><h3>Considerable Time For You</h3><p>Lorem ipsum dolor sit mork<br>adipiscing sed diam...[+]</p></div>
  <div class="feature right" style="left:88px;top:356px"><h3>Superior Advice</h3><p>Lorem ipsum dolor sit mork<br>adipiscing sed diam</p></div>
  <div class="feature" style="left:858px;top:343px"><h3>Deep Legal Industry<br>Relationships</h3><p>Lorem ipsum dolor sit mork<br>adipiscing sed diam...[+]</p></div>
  <div class="brand" style="top:380px;font-size:19px"><span class="mark"></span>Brindle's Homes</div>
</section>

<h2 class="script" style="top:2210px;font-size:37px">Lorem Ispum is the Dummy Text</h2>
<p class="intro">Lorem ipsum dolor sit amet, consectetuer adipiscing elit, sed reederiam nonummy nibh euismod tincidunt ut laoreet dolore&nbsp; lor emsmagna aliquam erat volutpat. Ut wisi enim fdaad minim veniam, quis nostrud exerci tation ullamcorper suscipit lobortis nisl ut aliquip ex ea commodo consequat.</p>
<h2 class="script" style="top:2333px;font-size:37px">Contact Us Today - 123.456.7890</h2>

<div class="desk" role="img" aria-label="Top-down photo of a white desk with keyboard, notepad, pencil, coffee cup and plant"></div>
<footer class="site-footer">
  <div class="brand"><span class="mark"></span>Brindle's Homes</div>
</footer>

<form class="form-card">
  <h2>Do You Have A Question?</h2>
  <div class="rule"></div>
  <p class="note">Lorem Ipsum is simply dummy text of the printing and typesetting industry. Lorem Ipsum has been the industry's standard dummy text ever since the 1500s.</p>
  <div class="field" style="left:55px;top:205px;width:269px;height:34px">Name</div>
  <div class="field" style="left:338px;top:205px;width:269px;height:34px">Email</div>
  <div class="field" style="left:55px;top:254px;width:552px;height:85px">Message</div>
  <div class="submit">SUBMIT <svg width="16" height="10"><path d="M0 5h14M10 1l4 4-4 4" stroke="#fff" fill="none" stroke-width="1.3"/></svg></div>
  <div class="fold"></div>
</form>

<div class="contact-item" style="left:143px">
  <svg width="18" height="24" viewBox="0 0 18 24"><path d="M9 0a9 9 0 0 0-9 9c0 7 9 15 9 15s9-8 9-15a9 9 0 0 0-9-9z" fill="#fff"/><circle cx="9" cy="9" r="3.5" fill="#1c1c1c"/></svg>
  <span>Street Name, City Name<br>State Zipcode</span>
</div>
<div class="contact-item" style="left:388px">
  <svg width="30" height="30" viewBox="0 0 26 26"><circle cx="13" cy="13" r="12" fill="none" stroke="#fff" stroke-width="1.5"/><path d="M9 7c-2 2-1 7 3 11 2 2 4 2 5 1l-2-3-2 1c-1-1-3-3-3-5l1-1-2-4z" fill="#fff"/></svg>
  <span>Call Us Today<br>&nbsp;&nbsp;123.456.7890</span>
</div>
<div class="contact-item" style="left:575px">
  <svg width="30" height="20" viewBox="0 0 30 20"><rect width="30" height="20" rx="2" fill="#fff"/><path d="M1 2l14 10L29 2" stroke="#1c1c1c" stroke-width="2" fill="none"/></svg>
  <span>Email<br>&nbsp;inquiry@brindleshomes.example</span>
</div>

<div class="bottom-bar"></div>
<p class="copyright">Copyright © 2018 Brindle's Homes.&nbsp; All Rights Reserved.</p>
<span class="social" style="left:918px"></span>
<span class="social" style="left:956px"></span>
<span class="social" style="left:993px"></span>
<span class="social" style="left:1031px"></span>

</body>
</html>
```